Join Wait / Reservations Handout

This is a handout for guests with information about the ability to join our
waitlist and/or make reservations. It will be handed out to any guest that ends up waiting on our waitlist to be seated. It will describe how our waitlist and reservations system works. It is informational for them to download our mobile app.

It was forcing me to move the look and feel sliders. Please refer to our branding guide for look and feel.

Industry/Entity Type

Hospitality

Contact Information for Business Card

One of the attached documents give a very generic layout of the information we need on this card. This layout is more for where we wanted the information placed and has nothing to do with the design aspects of the piece. Please use your imagination. Any of the 5 colors in the branding guide can be used anywhere. The pineapple design can be used anywhere in any color combination.

If you require any other files please let me know. Thanks

Font styles to use
Other font styles liked:
• Please see attached branding guide

Requirements
Must have
• The only color requirement is that the logo be the blue with teal lettering...This has to match our app store logo.

```html
<!DOCTYPE html>
<html lang="en">
<head>
<meta charset="utf-8">
<title>Join the Wait – Reservations Handout</title>
<link rel="stylesheet" href="https://fonts.googleapis.com/css2?family=Jost:ital,wght@0,400;0,500;1,400&display=swap">
<style>
  :root {
    --navy: #06334a;
    --ink: #0b3550;
    --teal: #62abae;
    --paper: #ffffff;
    --backdrop: #b3b3b6;
    --pattern-tone: #0d3d55;
  }
  * { box-sizing: border-box; margin: 0; padding: 0; }
  html, body {
    width: 1146px; height: 1200px; overflow: hidden;
    background: var(--backdrop);
    font-family: "Jost", "Futura", sans-serif;
  }
  .canvas { position: relative; width: 1146px; height: 1200px; }
  .card {
    position: absolute; top: 237px; width: 421px; height: 737px;
    text-align: center; text-transform: uppercase;
  }
  .card--front { left: 118px; background: var(--navy); color: var(--paper); overflow: hidden; }
  .card--back { left: 586px; background: var(--paper); color: var(--ink); }

  .front-pattern {
    position: absolute; inset: 0;
    background: linear-gradient(160deg, var(--pattern-tone), var(--navy) 55%, var(--pattern-tone));
  }
  .brand-badge {
    position: absolute; left: 52px; top: 59px; width: 320px; height: 320px;
    border-radius: 50%; background: var(--navy);
    display: flex; align-items: center; justify-content: center;
  }
  .brand-name {
    color: var(--teal); font-weight: 500; font-size: 38px; line-height: 1.1;
    letter-spacing: 2px;
  }
  .tagline {
    position: absolute; left: 0; right: 0; top: 418px;
    font-size: 32px; font-weight: 400; line-height: 48px; letter-spacing: 0.5px;
  }
  .front-rule {
    position: absolute; left: 42px; width: 342px; top: 560px; height: 5px; background: var(--teal);
  }
  .search-label {
    position: absolute; left: 0; right: 0; top: 603px; font-size: 21px; letter-spacing: 0.5px;
  }
  .search-query {
    position: absolute; left: 0; right: 0; top: 644px; font-size: 21px; font-style: italic; letter-spacing: 0.5px;
  }

  .info-block { position: absolute; left: 0; right: 0; }
  .info-heading { font-size: 22px; font-weight: 500; letter-spacing: 0.3px; line-height: 28px; }
  .info-answer { font-size: 22px; font-weight: 500; line-height: 28px; }
  .info-note { font-size: 16px; font-weight: 500; line-height: 20px; }
  .back-rule {
    position: absolute; left: 34px; width: 344px; height: 5px; background: var(--teal);
  }
</style>
</head>
<body>
<main class="canvas">
  <section class="card card--front">
    <div class="front-pattern" role="img" aria-label="Faint geometric diamond pattern in navy tones"></div>
    <div class="brand-badge"><span class="brand-name">HARBOR<br>TABLE</span></div>
    <p class="tagline">Save the wait…<br>Download our app</p>
    <div class="front-rule"></div>
    <p class="search-label">Search</p>
    <p class="search-query">“Harbor Table Eastfield”</p>
  </section>

  <section class="card card--back">
    <div class="info-block" style="top:51px">
      <p class="info-heading">When to join the wait?</p>
    </div>
    <div class="info-block" style="top:111px">
      <p class="info-answer">Anytime</p>
    </div>
    <div class="back-rule" style="top:179px"></div>

    <div class="info-block" style="top:219px">
      <p class="info-heading">When to reserve?</p>
    </div>
    <div class="info-block" style="top:278px">
      <p class="info-answer">Anytime - 2 hours in advance</p>
      <p class="info-note">(Excluding weekends, open-2pm)</p>
    </div>
    <div class="back-rule" style="top:369px"></div>

    <div class="info-block" style="top:412px">
      <p class="info-answer">Sunday</p>
      <p class="info-answer">+</p>
      <p class="info-answer" style="margin-top:2px">Holiday buffets</p>
      <p class="info-note">(Coming June 2018)</p>
    </div>
    <div class="back-rule" style="top:559px"></div>

    <div class="info-block" style="top:606px">
      <p class="info-answer">Large groups<br>handled/contacted<br>by catering manager</p>
    </div>
  </section>
</main>
</body>
</html>
```